This book will apply the 12 Steps to gaming addiction, also known as video game addiction. The primary purpose of the book is to provide an effective solution for this new type of addiction. The solution is based on the rich and successful concepts of traditional twelve-step programs like RL.

The title on the cover will be "Nine Doors Past the Glowing Screen" and "by Martin Quorby". A subtitle can be used if it works in your design of "A Practical Path Beyond Compulsive Console Play". Cover will be for a 6" x 9" book approximately 110 pages in length.

Some back cover text including some review quotes and an author bio are in the attached Word doc. There is also an author photo attached for for the back cover.

Requirements
Must have
• For the cover design it could be stylized, or an image, a partial image, or whatever. I am open to suggestions. Think about what would be noticed by a person searching for help with moderating their video game use, or by the parents or loved ones of problem gamers. Something contemporary and eye catching.

```html
<!DOCTYPE html>
<html lang="en">
<head>
<meta charset="utf-8">
<title>Nine Doors Past the Glowing Screen — Martin Quorby</title>
<link rel="stylesheet" href="https://fonts.googleapis.com/css2?family=Audiowide&display=swap">
<style>
  :root {
    --backdrop: #7a1214;
    --cover-black: #0a0a0b;
    --cover-deep: #0d1030;
    --title-cyan: #14d8f5;
    --accent-red: #ec1c24;
    --scene-blue: #3346c0;
    --scene-mid: #23288a;
    --scene-violet: #3a2478;
    --scene-red: #a3202e;
  }
  * { margin: 0; padding: 0; box-sizing: border-box; }
  html, body {
    width: 1200px;
    height: 1200px;
    overflow: hidden;
    background: var(--backdrop);
  }
  .canvas {
    position: relative;
    width: 1200px;
    height: 1200px;
    display: flex;
    align-items: center;
    justify-content: center;
  }
  .book-cover {
    position: relative;
    width: 734px;
    height: 1100px;
    background: var(--cover-black);
    overflow: hidden;
    font-family: "Audiowide", sans-serif;
  }
  .cover-art {
    position: absolute;
    left: 0;
    top: 360px;
    width: 100%;
    height: 640px;
    background:
      radial-gradient(ellipse 38% 22% at 62% 14%, rgba(190, 35, 50, 0.75), transparent 75%),
      radial-gradient(ellipse 34% 28% at 46% 38%, rgba(90, 120, 240, 0.85), transparent 75%),
      radial-gradient(ellipse 46% 20% at 50% 72%, rgba(80, 110, 235, 0.9), transparent 75%),
      radial-gradient(ellipse 80% 70% at 50% 50%, var(--scene-violet), transparent 85%),
      linear-gradient(to bottom, var(--scene-mid), var(--cover-deep));
    -webkit-mask-image: linear-gradient(to bottom, transparent 0%, #000 10%, #000 84%, transparent 100%);
            mask-image: linear-gradient(to bottom, transparent 0%, #000 10%, #000 84%, transparent 100%);
  }
  .title-block {
    position: absolute;
    left: 0;
    top: 70px;
    width: 100%;
    text-align: center;
    transform: rotate(-7deg);
    transform-origin: 50% 50%;
    line-height: 0.95;
    text-transform: uppercase;
    font-style: italic;
  }
  .title-line { display: block; color: var(--title-cyan); }
  .title-line--lead { font-size: 82px; letter-spacing: 1px; }
  .title-line--lead .title-accent { color: var(--accent-red); }
  .title-line--mid { font-size: 50px; margin-top: 6px; }
  .title-line--small { font-size: 40px; margin-top: 4px; }
  .title-line--big { font-size: 106px; margin-top: 2px; letter-spacing: -1px; }
  .subtitle {
    display: block;
    margin-top: 6px;
    font-size: 15.5px;
    letter-spacing: 0.5px;
    color: var(--accent-red);
  }
  .author-name {
    position: absolute;
    left: 0;
    bottom: 72px;
    width: 100%;
    text-align: center;
    font-size: 40px;
    font-style: italic;
    text-transform: uppercase;
    color: var(--accent-red);
    transform: rotate(-4deg);
  }
</style>
</head>
<body>
  <main class="canvas">
    <article class="book-cover">
      <div class="cover-art" role="img" aria-label="Dim blue-lit photograph of a hooded gamer gripping a wired controller beneath a glowing red pixel 'game over' sign"></div>

      <h1 class="title-block">
        <span class="title-line title-line--lead">Nine <span class="title-accent">Doors</span></span>
        <span class="title-line title-line--mid">Past the</span>
        <span class="title-line title-line--small">Glowing</span>
        <span class="title-line title-line--big">Screen</span>
        <span class="subtitle">A Practical Path Beyond Compulsive Console Play</span>
      </h1>

      <p class="author-name">Martin Quorby</p>
    </article>
  </main>
</body>
</html>
```